Online Psychiatry business - Business Card

I need a business card design. The target audience is busy professionals of any field (this therapy appeals best to 24-35 year olds). It involves psychiatry by tele-medicine (or video-conference). Nothing on it should be a giveaway that it's about mental health. Professional design with silver or gold as the primary colors appeals to me. The card must be as simple and as uncluttered as possible. Some color and flowing design on the edge of the card appeals to me.
CrestMindLink.com should probably appear in the center of the card and stand out, i.e. bold lettering, and easy to read, no cursive, but Ariel Black. Some where below this, should appear "No Spare Hour for Your Own Wellbeing? Not Anymore." Since this isn't office based, I don't think an office address is necessary and limits clutter.
Information that does need to appear is my name: Gerald Whitcombe, MD
General phone number: 541-876-2209. I'm hoping to get an 24-hour answering service soon so leave a little room for this. In addition I want to include two email addresses:
CrestMindLink@maildrop-box.com and CrestMind247@maildrop-box.com
Updates

I like the designs. I would like someone to put the website in bold in the center

 as most have been doing with a smaller font reminder nearby saying "No time" etc.
but I'd like to put my name down in the corner with the rest of the contact material.
Black print against a white or grey background appeals to me, with darker silver artwork near the sides (simple abstract, like wavy lines or something you can one up with that works. 
thanks

I ve tried to provide as much feedback as possible given my time limits, so if you have extra questions, please feel free to email. I tried to attach a file of a business card I really like but make be difficult to actually manufacture. I'm going to send you a link to the photo. The card has a pull tab. There is not much information on the outside. In fact, if you were to design the outside, I would just print : No Spare Hour for Your Own Wellbeing? Not Anymore.

When you pull the tab the remaining information is on the bottom half of the card. Please don't use the color pink!!!!
http://www.layoutgallerypost.com/2009/05/100-clever-card-ideas/
It is the 39th photo on the list, about 2/3ds of the way down the page. It is titled: Faltenkästli

#7 and #16 have an appeal to me, except for the dot patterns
Hope this helps

I'm running out of time and energy. I 've been trying to give do down the list and give  individual feedback but I won't be able to do that anymore.

So if you have any specific questions, write me, and again thank you for all your effort!!

I know i received your files, including your zip files, Plonix,

but Gideon, did you send me the files including ZIP on project 5914386?
thanks

Target Market(s)

Working professionals and executive, attorneys, etc.

Industry/Entity Type

Business

Logo Text

Don't Have Time to Take Care of Yourself? Think Again.

Logo styles of interest
Pictorial/Combination Logo
Wordmark Logo
Other font styles liked:
• Ariel Black appeals to me the most

Requirements
Must have
• Want to emphasize that the website must be obvious, easily found (The CrestMindLink.com)
For that reason i'd like the card to be white, and minimal decoration on one or both sides just to add some style and color
Nice to have
• A Very uncluttered, elegant design, and something that makes it stick in your head-doesn't everyone want the last?
Should not have
• Nothing on the card that give it away that this is about psychiatry, such as brain or other symbol, but also nothing that gives it away as a medical business, such as a stethoscope or red cross or anything.

```html
<!DOCTYPE html>
<html lang="en">
<head>
<meta charset="utf-8">
<title>CrestMindLink.com — Business Card</title>
<link rel="stylesheet" href="https://fonts.googleapis.com/css2?family=Archivo+Black&family=Arimo:wght@700&display=swap">
<style>
  :root {
    --card-bg: #e1e1e1;
    --card-edge: #8c8c8c;
    --band: #9b9b9b;
    --ink: #141414;
    --tile-light: #e4e4e4;
    --tile-dark: #d3d3d3;
  }
  * { margin: 0; padding: 0; box-sizing: border-box; }
  html, body { width: 1200px; height: 704px; overflow: hidden; background: #ffffff; }
  .card {
    position: relative;
    width: 1200px;
    height: 704px;
    background: var(--card-bg);
    border: 2px solid var(--card-edge);
    color: var(--ink);
    font-family: "Arimo", Arial, sans-serif;
    font-weight: 700;
  }
  .edge-texture {
    position: absolute;
    left: 0; top: 0;
    width: 100%; height: 60px;
    background: linear-gradient(180deg, var(--tile-dark) 0%, var(--tile-light) 65%, var(--card-bg) 100%);
  }
  .site-band {
    position: absolute;
    left: 0; top: 210px;
    width: 100%; height: 90px;
    background: var(--band);
    display: flex;
    align-items: center;
    justify-content: center;
  }
  .site-name {
    font-family: "Archivo Black", "Arial Black", sans-serif;
    font-weight: 400;
    font-size: 80px;
    line-height: 1;
    letter-spacing: 0.5px;
  }
  .tagline {
    position: absolute;
    right: 58px; top: 318px;
    font-size: 21px;
    white-space: nowrap;
  }
  .contact {
    position: absolute;
    left: 50px; top: 393px;
  }
  .contact-name {
    font-size: 35px;
    line-height: 1.1;
  }
  .contact-title {
    font-size: 18px;
    margin: 6px 0 0 5px;
  }
  .contact-phone {
    font-size: 29px;
    margin-top: 18px;
  }
  .footer-band {
    position: absolute;
    left: 0; top: 604px;
    width: 100%; height: 16px;
    background: var(--band);
  }
  .emails {
    position: absolute;
    left: 44px; right: 44px; top: 644px;
    display: flex;
    justify-content: space-between;
    font-size: 28px;
    letter-spacing: -0.2px;
    white-space: nowrap;
  }
</style>
</head>
<body>
  <div class="card">
    <div class="edge-texture" role="img" aria-label="Subtle grey tiled square texture along the top edge"></div>

    <div class="site-band">
      <h1 class="site-name">CrestMindLink.com</h1>
    </div>

    <p class="tagline">"No Spare Hour for Your Own Wellbeing? Not Anymore.”</p>

    <div class="contact">
      <p class="contact-name">Gerald Whitcombe</p>
      <p class="contact-title">MD</p>
      <p class="contact-phone">Phone : 541-876-2209</p>
    </div>

    <div class="footer-band"></div>

    <div class="emails">
      <span class="email">CrestMindLink@maildrop-box.com</span>
      <span class="email">CrestMind247@maildrop-box.com</span>
    </div>
  </div>
</body>
</html>
```